Business Card Design Project

We need a business card design for a management consultancy focused on financial innovation and digital money, run by experts from the Financial Services, Telecoms and Money Transfer industries.
Our products include services such as Mobile Payments, Mobile Money, Digital Wallets, Online Payments, Branchless Banking and more. We work with regulatory information, business plans, financial modelling, strategic planning, new products functional specification, new technologies evaluation, etc.
See company logo attached.
We would like to see 2 versions: one in portuguese and one in english (regarding data information). You can see below information needed (whenever there is a difference between the two versions, the first one is in english and the second one in portuguese).

Name
Position
Phone/ Tel: ++55-11-xxxx-xxxx
Cell/ Cel: ++55-11-9 xxxx-xxxx
Dr. Tavares Lobato Av., 318 - Tower II - 16th floor / Avenida Dr. Tavares Lobato, 318 - Torre II - 16o. andar
São Paulo - SP
01327-118 - Brazil/ 01327-118 - Brasil

Target Market(s)

Audience: C-level executives from banks, credit card companies, acquirers, IT developers, retailers

Industry/Entity Type

Financial

Requirements
Must have
• Must use the logo and information above. Front must have white background. Back side should have only logo.
Nice to have
• Back should be in another colour but if it seems too exxagerated, maintain back in white also.
Should not have
• Do not add other illustrations to the business card.

```html
<!DOCTYPE html>
<html lang="pt">
<head>
<meta charset="utf-8">
<title>R Almeida – Cartão de Visita</title>
<link href="https://fonts.googleapis.com/css2?family=Cinzel:wght@400;600&family=Open+Sans:wght@400;600&display=swap" rel="stylesheet">
<style>
  :root {
    --backdrop: #e4e4e4;
    --card: #ffffff;
    --navy: #1f2f78;
    --ink: #1e1e1e;
    --rule: #1f2f78;
  }
  html, body {
    margin: 0;
    width: 1200px;
    height: 675px;
    overflow: hidden;
    background: var(--backdrop);
  }
  .card {
    position: absolute;
    left: 250px;
    top: 137px;
    width: 700px;
    height: 400px;
    background: var(--card);
    box-shadow: 0 2px 10px rgba(0,0,0,0.08);
    font-family: "Open Sans", Arial, sans-serif;
    color: var(--ink);
  }
  .brand {
    position: absolute;
    right: 40px;
    top: 62px;
    display: flex;
    align-items: center;
    gap: 12px;
    font-family: "Cinzel", Georgia, serif;
    font-weight: 600;
    font-size: 34px;
    letter-spacing: 1px;
    color: var(--ink);
  }
  .brand-square {
    width: 30px;
    height: 30px;
    background: var(--navy);
  }
  .rule {
    position: absolute;
    height: 2px;
    background: var(--rule);
  }
  .rule-top { left: 260px; right: 35px; top: 136px; }
  .rule-bottom { left: 50px; right: 35px; top: 300px; }
  .person-name {
    position: absolute;
    left: 50px;
    top: 128px;
    font-family: "Cinzel", Georgia, serif;
    font-size: 21px;
    color: var(--navy);
    letter-spacing: 0.5px;
  }
  .person-role {
    position: absolute;
    left: 50px;
    top: 160px;
    font-size: 13px;
  }
  .contact {
    position: absolute;
    left: 50px;
    display: flex;
    align-items: center;
    gap: 14px;
    font-size: 15px;
  }
  .contact svg { width: 16px; height: 16px; fill: var(--navy); }
  .phone-line { top: 246px; }
  .cell-line { top: 270px; }
  .address {
    position: absolute;
    left: 80px;
    top: 312px;
    font-size: 15px;
    line-height: 24px;
  }
  .postcode { color: var(--navy); }
  .pin {
    position: absolute;
    left: 50px;
    top: 342px;
    width: 16px;
    height: 18px;
    fill: var(--navy);
  }
</style>
</head>
<body>
  <div class="card">
    <div class="brand"><span class="brand-square"></span>R Almeida</div>
    <div class="rule rule-top"></div>
    <div class="person-name">Your Long Name</div>
    <div class="person-role">Director</div>

    <div class="contact phone-line">
      <svg viewBox="0 0 16 16" aria-hidden="true"><path d="M4 1h8a1 1 0 0 1 1 1v12a1 1 0 0 1-1 1H4a1 1 0 0 1-1-1V2a1 1 0 0 1 1-1zm1 2v9h6V3zm3 10a.8.8 0 1 0 0 .01z"/></svg>
      <span>++55-11-xxxx-xxxx</span>
    </div>
    <div class="contact cell-line">
      <svg viewBox="0 0 16 16" aria-hidden="true"><path d="M2 5c0-2 3-3 6-3s6 1 6 3v1h-3V5H5v1H2zm2 2h8l2 7H2zm4 1.5a2 2 0 1 0 0 4 2 2 0 0 0 0-4z"/></svg>
      <span>++55-11-9 xxxx-xxxx</span>
    </div>

    <div class="rule rule-bottom"></div>

    <svg class="pin" viewBox="0 0 16 18" aria-hidden="true"><path d="M8 0a6 6 0 0 1 6 6c0 4.5-6 12-6 12S2 10.5 2 6a6 6 0 0 1 6-6zm0 3.5a2.5 2.5 0 1 0 0 5 2.5 2.5 0 0 0 0-5z"/></svg>
    <div class="address">
      <div>Dr. Tavares Lobato, 318 - Torre II -16o. andar São Paulo - SP</div>
      <div class="postcode">01327-118 - Brazil</div>
    </div>
  </div>
</body>
</html>
```